Research, Writing and Editing business needs a Business Card Design

I need a business card design for a new company based in Melbourne called The Bellwood Advisory Group. We provide research, writing and editing services. The company logo is attached, but I am open to your creative designs for business cards with the logo. As you will note, there are two potential logos. Feel free to use either of the logos.

The overall look I am hoping for is sleek, sophisticated, feminine and elegant.

Thanks in advance for your efforts.

Target Market(s)

Business professionals, academics and students

Industry/Entity Type

Business

Font styles to use
Serif
Script

Colors

Designer to choose colors to be used in the design.

Requirements
Must have
• The Bellwood Advisory Group
Dr Tessa Brennig

M: 0458 293 647
E: tessa@thebellwoodadvisorygroup.com.au
W: thebellwoodadvisorygroup.com.au
Nice to have
• Research | Writing | Editing

```html
<!DOCTYPE html>
<html lang="en">
<head>
<meta charset="utf-8">
<title>The Bellwood Advisory Group – Business Card</title>
<link rel="stylesheet" href="https://fonts.googleapis.com/css2?family=Raleway:wght@400;700&family=Roboto:wght@400&display=swap">
<style>
  :root {
    --backdrop: #d8d8da;
    --card-white: #fbfbfb;
    --card-grey: #ececec;
    --ink: #141414;
    --ink-soft: #2a2a2a;
    --paper-text: #f4f4f4;
  }
  * { box-sizing: border-box; margin: 0; padding: 0; }
  html, body { width: 1200px; height: 900px; overflow: hidden; }
  body {
    background: var(--backdrop);
    font-family: "Roboto", Arial, sans-serif;
    color: var(--ink);
    position: relative;
  }
  .card {
    position: absolute;
    left: 250px;
    width: 700px;
    height: 400px;
    box-shadow: 0 6px 18px rgba(0,0,0,0.18);
  }
  /* Front */
  .card-front {
    top: 35px;
    background: var(--card-white);
    display: flex;
    flex-direction: column;
    align-items: center;
    justify-content: center;
    gap: 26px;
  }
  .brand {
    display: flex;
    align-items: center;
    gap: 18px;
  }
  .brand-mark {
    width: 34px;
    height: 34px;
    background: var(--ink);
  }
  .brand-name {
    font-family: "Raleway", Arial, sans-serif;
    font-weight: 400;
    font-size: 30px;
    letter-spacing: 4px;
    text-transform: uppercase;
    color: var(--ink);
  }
  .tagline {
    font-family: "Raleway", Arial, sans-serif;
    font-weight: 400;
    font-size: 15px;
    letter-spacing: 5px;
    text-transform: uppercase;
    color: var(--ink-soft);
  }
  /* Back */
  .card-back {
    top: 465px;
    background: var(--ink);
    padding: 26px;
  }
  .back-panel {
    width: 100%;
    height: 100%;
    background: linear-gradient(135deg, #f6f6f6 0%, var(--card-grey) 100%);
    position: relative;
  }
  .back-brand {
    position: absolute;
    top: 38px;
    right: 40px;
    display: flex;
    align-items: center;
    gap: 12px;
  }
  .back-brand .brand-mark { width: 22px; height: 22px; }
  .back-brand .brand-name { font-size: 18px; letter-spacing: 3px; }
  .name-pill {
    position: absolute;
    top: 140px;
    left: 0;
    width: 430px;
    height: 52px;
    background: var(--ink);
    border-radius: 0 26px 26px 0;
    display: flex;
    align-items: center;
    padding-left: 40px;
  }
  .person-name {
    font-family: "Raleway", Arial, sans-serif;
    font-weight: 700;
    font-size: 26px;
    letter-spacing: 2px;
    text-transform: uppercase;
    color: var(--paper-text);
  }
  .contact-list {
    position: absolute;
    left: 40px;
    top: 222px;
    list-style: none;
    display: flex;
    flex-direction: column;
    gap: 12px;
  }
  .contact-item {
    display: flex;
    align-items: center;
    gap: 14px;
    font-size: 17px;
    color: var(--ink);
  }
  .contact-icon { width: 20px; height: 20px; flex: none; }
</style>
</head>
<body>
  <section class="card card-front" aria-label="Business card front">
    <div class="brand">
      <span class="brand-mark"></span>
      <span class="brand-name">The Bellwood Advisory Group</span>
    </div>
    <p class="tagline">Research | Writing | Editing</p>
  </section>

  <section class="card card-back" aria-label="Business card back">
    <div class="back-panel">
      <div class="back-brand">
        <span class="brand-mark"></span>
        <span class="brand-name">The Bellwood Advisory Group</span>
      </div>

      <div class="name-pill">
        <h1 class="person-name">Dr Tessa Brennig</h1>
      </div>

      <ul class="contact-list">
        <li class="contact-item">
          <svg class="contact-icon" viewBox="0 0 20 20" aria-hidden="true">
            <rect x="5" y="1" width="10" height="18" rx="2" fill="none" stroke="#141414" stroke-width="2"/>
            <circle cx="10" cy="15.5" r="1.2" fill="#141414"/>
          </svg>
          <span>0458 293 647</span>
        </li>
        <li class="contact-item">
          <svg class="contact-icon" viewBox="0 0 20 20" aria-hidden="true">
            <rect x="1" y="4" width="18" height="12" rx="1.5" fill="#141414"/>
            <path d="M2 5 L10 11 L18 5" fill="none" stroke="#ececec" stroke-width="1.6"/>
          </svg>
          <span>tessa@thebellwoodadvisorygroup.com.au</span>
        </li>
        <li class="contact-item">
          <svg class="contact-icon" viewBox="0 0 20 20" aria-hidden="true">
            <circle cx="10" cy="10" r="8.5" fill="none" stroke="#141414" stroke-width="1.8"/>
            <ellipse cx="10" cy="10" rx="3.6" ry="8.5" fill="none" stroke="#141414" stroke-width="1.4"/>
            <line x1="1.5" y1="10" x2="18.5" y2="10" stroke="#141414" stroke-width="1.4"/>
          </svg>
          <span>thebellwoodadvisorygroup.com.au</span>
        </li>
      </ul>
    </div>
  </section>
</body>
</html>
```